Harbor Crest Industrial Services Brochure

-Need a tri-fold brochure, please use our new website colors and theme (I will attach a screen shot as it not live yet).
- Same layout as old brochure will work but I want to match our new website design (I will attach).
-I have attached our old brochure with pen written edits
-We need to add a valve section, if you can find a better image similar to what I attache that would be great.
-I want to replace the BOP stack image with some large refiner tank image, they are usually white tanks. Ill attached a sample picture.
-I will like to replace the front cover spray gun image with sandblaster balsting the 2 large pipes.
-you can use other same images or find good replacments but they have express a fresh paint job.
-Replace structual picture with yellow/orange frame picture attached
Updates
Also add Oven Cured Coatings to Surface Coating section.
Target Market(s)
Industrial customers
Industry/Entity Type
oil & gas, refinery, heavy equipment
Look and feel

```html
<!DOCTYPE html>
<html lang="en">
<head>
<meta charset="utf-8">
<title>Harbor Crest Industrial Services – Tri-fold Brochure</title>
<link href="https://fonts.googleapis.com/css2?family=Open+Sans:ital,wght@0,400;0,600;0,700;0,800;1,400;1,600;1,700&family=Oswald:wght@600;700&display=swap" rel="stylesheet">
<style>
  :root{
    --blue:#1f5fae;
    --blue-deep:#174a8c;
    --ink:#2b2b2b;
    --charcoal:#3a3a3c;
    --paper:#ffffff;
    --paper-soft:#f3f3f3;
    --backdrop:#e4e4e4;
    --photo-warm:#c9b29a;
    --photo-cool:#9aa3ad;
  }
  *{box-sizing:border-box;margin:0;padding:0}
  html,body{width:1200px;height:2400px;overflow:hidden;background:var(--backdrop)}
  body{position:relative;font-family:"Open Sans",Arial,sans-serif;color:var(--ink)}

  .spread{position:absolute;left:50px;width:1100px;height:850px;background:var(--paper);box-shadow:0 6px 24px rgba(0,0,0,.18);overflow:hidden}
  .spread--outside{top:230px}
  .spread--inside{top:1320px}
  .panel{position:absolute;top:0;width:366.67px;height:850px;overflow:hidden}
  .panel--1{left:0}
  .panel--2{left:366.67px}
  .panel--3{left:733.33px}
  .fold{position:absolute;top:0;width:1px;height:850px;background:rgba(0,0,0,.08);z-index:5}

  .photo{position:absolute}
  .shape{position:absolute;left:0;top:0}

  /* coatings list */
  .coatings-title{position:absolute;left:48px;top:52px;font-style:italic;font-weight:700;font-size:25px;color:var(--blue)}
  .coatings-rule{position:absolute;left:48px;top:94px;width:200px;height:2px;background:var(--blue)}
  .coatings-list{position:absolute;left:66px;top:116px;list-style:none;font-style:italic;font-size:18px;line-height:31px}
  .coatings-list li::before{content:"";display:inline-block;width:6px;height:6px;border-radius:50%;background:var(--blue);margin:0 12px 3px -20px;vertical-align:middle}

  .badges{position:absolute;left:48px;top:500px;display:flex;gap:22px}
  .badge{width:60px;height:40px;background:var(--blue-deep);border-radius:4px}
  .badge--round{width:44px;height:44px;border-radius:50%;background:var(--charcoal)}

  /* back panel */
  .quote{position:absolute;left:0;right:0;top:640px;text-align:center;color:var(--paper)}
  .quote-tag{display:inline-block;border:2px solid var(--paper);padding:6px 18px;font-weight:800;font-size:18px;letter-spacing:.5px}
  .quote-address{margin-top:18px;font-size:15px}
  .quote-phone{font-size:13px;font-style:italic;opacity:.9;margin-top:2px}
  .quote-email{margin-top:22px;font-size:17px;font-weight:700}

  /* cover */
  .brand{position:absolute;left:44px;top:42px;display:flex;align-items:center;gap:14px}
  .brand-mark{width:50px;height:50px;background:var(--blue)}
  .brand-name{font-weight:700;font-size:19px;line-height:22px;color:var(--blue)}
  .cover-slogan{position:absolute;left:0;right:0;top:650px;text-align:center;font-family:"Oswald",Impact,sans-serif;font-weight:700;font-size:30px;line-height:34px;color:var(--ink);text-transform:uppercase}
  .cover-url{position:absolute;left:50%;top:740px;transform:translateX(-50%);border:3px solid var(--blue);padding:8px 18px;font-weight:700;font-size:19px;color:var(--ink);white-space:nowrap}

  /* inside middle */
  .areas{position:absolute;left:0;right:0;top:44px;color:var(--paper)}
  .area-tag{display:block;width:max-content;margin:0 auto;border:2px solid var(--paper);padding:5px 16px;font-weight:700;font-size:16px}
  .area-list{list-style:none;margin:18px 34px 30px 50px;font-size:14.5px;line-height:21px}
  .area-list li{margin-bottom:6px}
  .area-list li::before{content:"";display:inline-block;width:5px;height:5px;border-radius:50%;background:var(--paper);margin:0 10px 3px -16px;vertical-align:middle}

  /* inside right */
  .services{position:absolute;left:38px;top:350px;right:28px;color:var(--blue)}
  .services-heading{font-weight:800;font-size:21px;line-height:25px;text-transform:uppercase}
  .services-sub{margin-top:18px;font-weight:800;font-size:15px;text-transform:uppercase}
  .services-list{list-style:none;margin:8px 0 0 18px;font-size:14.5px;line-height:21px;color:var(--ink)}
  .services-list li::before{content:"";display:inline-block;width:5px;height:5px;border-radius:50%;background:var(--blue);margin:0 10px 3px -15px;vertical-align:middle}
  .thumbs{position:absolute;left:38px;top:660px;display:flex;gap:20px}
  .thumb{width:135px;height:95px;border:4px solid var(--blue);background:linear-gradient(160deg,#a9c4de,#d59a3f 70%,#7a6a55)}
</style>
</head>
<body>

<!-- OUTSIDE SPREAD -->
<section class="spread spread--outside" aria-label="Brochure outside">
  <div class="fold" style="left:366px"></div>
  <div class="fold" style="left:733px"></div>

  <!-- inside flap -->
  <div class="panel panel--1">
    <h2 class="coatings-title">Surface Coatings</h2>
    <div class="coatings-rule"></div>
    <ul class="coatings-list">
      <li>Epoxy Coatings</li><li>Urethane Coatings</li><li>Zinc Primers</li><li>Tank Linings</li>
      <li>Non-Skid Coatings</li><li>High Temp Coatings</li><li>Floor Coatings</li><li>Fireproof Coatings</li>
      <li>Polyurea</li><li>Powder Coatings</li><li>Oven Cured Coatings</li>
    </ul>
    <div class="badges" aria-label="Certification badges">
      <div class="badge"></div><div class="badge badge--round"></div>
    </div>
    <svg class="shape" width="367" height="850" viewBox="0 0 367 850" aria-hidden="true">
      <polygon points="0,640 367,575 367,850 0,850" fill="var(--blue)"/>
    </svg>
    <div class="photo" role="img" aria-label="Worker spray painting steel parts in a booth"
         style="left:0;top:600px;width:250px;height:250px;clip-path:polygon(0 10%,100% 0,100% 100%,0 100%);background:linear-gradient(135deg,#eef0f2,#b9c0c8 60%,#6f7782)"></div>
  </div>

  <!-- back panel -->
  <div class="panel panel--2" style="background:var(--blue)">
    <div class="photo" role="img" aria-label="Sandblaster working between two large steel pipes"
         style="left:0;top:0;width:367px;height:600px;background:linear-gradient(180deg,#f6f6f6 0%,#e2dcd4 50%,var(--photo-warm) 100%)"></div>
    <svg class="shape" width="367" height="850" viewBox="0 0 367 850" aria-hidden="true">
      <path d="M0,470 Q183,600 367,470 L367,850 L0,850 Z" fill="var(--blue)"/>
      <path d="M0,470 Q183,600 367,470" fill="none" stroke="var(--charcoal)" stroke-width="12"/>
    </svg>
    <div class="photo" role="img" aria-label="Freshly coated industrial valves and piping"
         style="left:113px;top:440px;width:140px;height:140px;border-radius:50%;border:6px solid var(--paper);background:radial-gradient(circle at 40% 40%,#9fb6c9,#4d6f8f 70%,#2c3e52)"></div>
    <div class="quote">
      <span class="quote-tag">NEED A QUOTE?</span>
      <p class="quote-address">4810 Millbrook Rd, Houston, TX 77099</p>
      <p class="quote-phone">Office: 281-555-0147</p>
      <p class="quote-email">quotes@harborcrestind.com</p>
    </div>
  </div>

  <!-- cover -->
  <div class="panel panel--3">
    <div class="brand">
      <div class="brand-mark"></div>
      <div class="brand-name">Harbor Crest<br>Industrial Services</div>
    </div>
    <div class="photo" role="img" aria-label="Sandblaster blasting two large pipes"
         style="left:0;top:125px;width:367px;height:480px;clip-path:polygon(0 0,100% 0,100% 70%,0 100%);background:linear-gradient(170deg,#f7f7f7 0%,#e6e1db 45%,var(--photo-warm) 100%)"></div>
    <svg class="shape" width="367" height="850" viewBox="0 0 367 850" aria-hidden="true">
      <line x1="0" y1="605" x2="367" y2="461" stroke="var(--charcoal)" stroke-width="14"/>
      <polygon points="367,420 367,520 230,520" fill="var(--blue)"/>
      <polygon points="0,850 0,790 70,850" fill="var(--blue)"/>
    </svg>
    <h1 class="cover-slogan">Commited to<br>Quality &amp; Compliance</h1>
    <div class="cover-url">www.HarborCrestInd.com</div>
  </div>
</section>

<!-- INSIDE SPREAD -->
<section class="spread spread--inside" aria-label="Brochure inside">
  <div class="fold" style="left:366px"></div>
  <div class="fold" style="left:733px"></div>

  <div class="panel panel--1">
    <h2 class="coatings-title">Surface Coatings</h2>
    <div class="coatings-rule"></div>
    <ul class="coatings-list">
      <li>Epoxy Coatings</li><li>Urethane Coatings</li><li>Zinc Primers</li><li>Tank Linings</li>
      <li>Non-Skid Coatings</li><li>High Temp Coatings</li><li>Floor Coatings</li><li>Fireproof Coatings</li>
      <li>Polyurea</li><li>Powder Coatings</li><li>Oven Cured Coatings</li>
    </ul>
    <svg class="shape" width="367" height="850" viewBox="0 0 367 850" aria-hidden="true">
      <polygon points="0,590 170,590 0,680" fill="var(--blue)"/>
    </svg>
    <div class="photo" role="img" aria-label="Large steel pipe being blasted to bare metal"
         style="left:0;top:600px;width:367px;height:250px;clip-path:polygon(0 40%,100% 10%,100% 100%,0 100%);background:linear-gradient(160deg,#d9d6d2,#b5764a 55%,#6e4a33)"></div>
  </div>

  <div class="panel panel--2" style="background:var(--blue)">
    <div class="areas">
      <span class="area-tag">Surface Preparation Areas</span>
      <ul class="area-list">
        <li>1 - Blast Enclosure 75' W x 60' L x 28' H (4,500 sqft)</li>
        <li>5+ Acres of Outdoor Blast Area for items in excess of 15' in Length or Width</li>
      </ul>
      <span class="area-tag">Coating Areas</span>
      <ul class="area-list">
        <li>1 - Large Spray Booth 50' x 120'</li>
        <li>2 - Large Spray Booths 75' x 60'</li>
        <li>1 - Mid Size Booth 35' x 30'</li>
        <li>20,000 sqft of Total Coating Booth</li>
        <li>7 acres of Laydown Yard</li>
      </ul>
    </div>
    <div class="photo" role="img" aria-label="Worker in protective suit blasting a steel surface"
         style="left:0;top:560px;width:367px;height:290px;clip-path:polygon(0 30%,100% 0,100% 100%,0 100%);background:linear-gradient(160deg,#e9ecef,#aab2bb 55%,#5b636d)"></div>
  </div>

  <div class="panel panel--3">
    <div class="photo" role="img" aria-label="Heavy forklift lifting equipment in a yard"
         style="left:0;top:0;width:367px;height:330px;clip-path:polygon(0 0,100% 0,100% 100%,0 70%);background:linear-gradient(180deg,#cfd8e2,#6f7c8a 60%,#3d4650)"></div>
    <svg class="shape" width="367" height="850" viewBox="0 0 367 850" aria-hidden="true">
      <polygon points="367,250 367,330 250,330" fill="var(--blue)"/>
      <polygon points="0,850 0,780 90,850" fill="var(--blue)"/>
    </svg>
    <div class="services">
      <h2 class="services-heading">Lifting Capacity of<br>125,000 LBS</h2>
      <h3 class="services-sub">Inhouse and Field Services</h3>
      <ul class="services-list">
        <li>24 hours a day, 7 days a week</li>
        <li>Mobile equipment on standby</li>
      </ul>
      <h3 class="services-sub">Easy Access To</h3>
      <ul class="services-list">
        <li>Beltway 8</li>
        <li>Houston Ports</li>
        <li>IAH and Hobby Airports</li>
      </ul>
    </div>
    <div class="thumbs">
      <div class="thumb" role="img" aria-label="Yellow and orange steel frame after coating"></div>
      <div class="thumb" role="img" aria-label="Orange heavy equipment in the laydown yard"></div>
    </div>
  </div>
</section>

</body>
</html>
```